Occupational Therapist does home accessibility for disabled folks; needs business card design

We need a business card for a company in Portland, Oregon that specializes in making homes accessible, comfortable, and functional for people who are disabled or aging who would like to stay in THEIR home. Our medical background as Occupational Therapists allows us to translate the functional needs of the person into the recommendations for the design of the home remodel.

Target Market(s)

Elderly, children of elderly
People with disabilities, families of people with disabilities

Industry/Entity Type

Business

Contact Information for Business Card

Company name: HomeWise
Name: Danielle Reyes Crawford, OTR/L, CAPS, ECHM
Occupational Therapist, Home Modification & Accessibility Specialist
website: www.homewiseforyears.com
email: homewiseforyears@nestmail.example
phone: (503)218-4057
CCB #: 487315

Font styles to use
Sans Serif

Requirements
Must have
• My logo
• Easy to read font with contrasting background
• Please list the Services offered: Occupational Therapy, Home safety & accessibility assessments, Home modification consulting, project management
Nice to have
• Friendly, welcoming feel
Should not have
• Dark colored background

```html
<!DOCTYPE html>
<html lang="en">
<head>
<meta charset="utf-8">
<title>HomeWise Business Card</title>
<link rel="stylesheet" href="https://fonts.googleapis.com/css2?family=Open+Sans:wght@400;600&display=swap">
<style>
  :root {
    --page-bg: #ecebe8;
    --card-bg: #ffffff;
    --ink-gray: #6d6e70;
    --ink-dark: #3a3a3c;
    --accent-orange: #d4892f;
    --accent-gold: #e0b23c;
    --rule: #8a8b8d;
  }
  * { box-sizing: border-box; margin: 0; padding: 0; }
  html, body {
    width: 1200px;
    height: 1200px;
    overflow: hidden;
    background: var(--page-bg);
    font-family: "Open Sans", Arial, sans-serif;
  }
  .sheet {
    width: 1200px;
    height: 1200px;
    display: flex;
    flex-direction: column;
    align-items: center;
    justify-content: center;
    gap: 60px;
  }
  .card {
    width: 880px;
    height: 503px;
    background: var(--card-bg);
    box-shadow: 0 6px 22px rgba(0,0,0,0.12);
    position: relative;
  }
  /* Front */
  .card-front {
    display: flex;
    align-items: center;
  }
  .front-brand {
    width: 390px;
    display: flex;
    justify-content: center;
  }
  .brand {
    display: flex;
    align-items: center;
    gap: 18px;
  }
  .brand-square {
    width: 44px;
    height: 44px;
    background: var(--accent-orange);
  }
  .brand-name {
    font-weight: 600;
    font-size: 52px;
    color: var(--ink-gray);
    letter-spacing: -0.5px;
  }
  .divider {
    width: 1.5px;
    height: 260px;
    background: var(--rule);
  }
  .front-details {
    padding-left: 48px;
    padding-right: 40px;
  }
  .person-name {
    font-size: 33px;
    font-weight: 400;
    color: var(--ink-gray);
    line-height: 1.15;
  }
  .credentials {
    font-size: 19px;
    color: var(--ink-dark);
    margin-top: 4px;
    letter-spacing: 0.3px;
  }
  .role {
    font-size: 18px;
    color: var(--accent-orange);
    line-height: 1.35;
    margin-top: 16px;
  }
  .contact {
    list-style: none;
    margin-top: 24px;
    font-size: 18px;
    color: var(--ink-dark);
    line-height: 1.5;
  }
  .contact .license {
    font-size: 15px;
    color: var(--ink-gray);
  }
  /* Back */
  .card-back {
    display: flex;
    flex-direction: column;
    align-items: center;
    justify-content: center;
    gap: 48px;
  }
  .card-back .brand-square {
    width: 64px;
    height: 64px;
    background: var(--accent-gold);
  }
  .card-back .brand-name {
    font-size: 76px;
  }
  .services {
    list-style: none;
    display: flex;
    flex-wrap: wrap;
    justify-content: center;
    gap: 8px 28px;
    max-width: 700px;
    font-size: 18px;
    color: var(--ink-dark);
    line-height: 1.4;
  }
  .services li {
    display: flex;
    align-items: center;
    gap: 10px;
  }
  .services li::before {
    content: "";
    width: 8px;
    height: 8px;
    background: var(--accent-gold);
  }
</style>
</head>
<body>
<main class="sheet">
  <section class="card card-front" aria-label="Business card front">
    <div class="front-brand">
      <div class="brand">
        <span class="brand-square" aria-hidden="true"></span>
        <span class="brand-name">HomeWise</span>
      </div>
    </div>
    <div class="divider" aria-hidden="true"></div>
    <div class="front-details">
      <h1 class="person-name">Danielle Reyes Crawford</h1>
      <p class="credentials">OTR/L, CAPS, ECHM</p>
      <p class="role">Occupational Therapist, Home<br>Modification &amp; Accessibility Specialist</p>
      <ul class="contact">
        <li>(503)218-4057</li>
        <li>www.homewiseforyears.com</li>
        <li>homewiseforyears@nestmail.example</li>
        <li class="license">CCB #: 487315</li>
      </ul>
    </div>
  </section>

  <section class="card card-back" aria-label="Business card back">
    <div class="brand">
      <span class="brand-square" aria-hidden="true"></span>
      <span class="brand-name">HomeWise</span>
    </div>
    <ul class="services" aria-label="Services">
      <li>Occupational Therapy</li>
      <li>Home Safety &amp; Accessibility Assessments</li>
      <li>Home Modification Consulting</li>
      <li>Project Management</li>
    </ul>
  </section>
</main>
</body>
</html>
```